Business card for Luxury Portable Restroom Trailer company

We are a Luxury Portable Restroom Trailer Company Called PELIKAR HIRES. Based in Orange County California. We provide portable restroom trailers for events, such as, Weddings, Concerts, Charity events, Sporting events, Tournaments, Corporate events, ect. We rent and Sell the Luxury restrooms. Our colors are white, grey, and Orange. As you will see in the logo we uploaded.
There are 2 people in the company so the names and titles will change for the 3 people but card will remain the same. Here is the information for each Person: Dennis Moyle CFO 555 018-3647
next Person: Wesley Tanford VP 555 018-3647
Next Person: Miles Tanford CEO 555 018-3647
Information to include on the card: Luxury Restroom Trailers Rental and Sales. Weddings, Concerts, Charity, Sporting and Corp. Events.

```html
<!DOCTYPE html>
<html lang="en">
<head>
<meta charset="utf-8">
<title>Pelikar Hires – Business Card</title>
<link href="https://fonts.googleapis.com/css2?family=Lato:wght@400;700;900&display=swap" rel="stylesheet">
<style>
  :root {
    --stage: #2b2c2e;
    --card: #555556;
    --orange: #f26b21;
    --white: #ffffff;
    --muted: #e9e9e9;
  }
  * { box-sizing: border-box; margin: 0; padding: 0; }
  html, body {
    width: 1200px; height: 952px; overflow: hidden;
    background: var(--stage);
    font-family: "Lato", sans-serif;
  }
  .stage {
    width: 1200px; height: 952px;
    display: flex; flex-direction: column;
    align-items: center; justify-content: center; gap: 30px;
  }
  .card {
    position: relative;
    width: 760px; height: 434px;
    background: var(--card);
    border-radius: 26px;
    overflow: hidden;
  }

  /* Front */
  .brand-name {
    position: absolute; left: 150px; top: 46px;
    color: var(--orange);
    font-weight: 900; font-size: 40px; letter-spacing: 3px;
  }
  .contacts {
    position: absolute; left: 70px; top: 150px;
    list-style: none;
    color: var(--muted); font-size: 15px; line-height: 1.3;
  }
  .contacts li { display: flex; align-items: flex-start; gap: 12px; margin-bottom: 10px; }
  .contact-icon {
    flex: none; width: 18px; height: 18px; border-radius: 3px;
    background: var(--white); display: flex; align-items: center; justify-content: center;
  }
  .contact-icon.is-accent { background: var(--orange); }
  .accent-rule {
    position: absolute; left: 0; top: 318px;
    width: 300px; height: 4px; background: var(--orange);
  }
  .services {
    position: absolute; left: 70px; top: 342px; width: 420px;
    color: var(--muted); font-size: 14px; line-height: 1.45;
  }
  .services strong { color: var(--orange); font-weight: 700; }
  .person {
    position: absolute; right: 70px; top: 170px; text-align: right;
  }
  .person-name {
    color: var(--orange); font-size: 28px; letter-spacing: 1px; font-weight: 400;
  }
  .person-name strong { font-weight: 900; }
  .person-title {
    color: var(--white); font-size: 20px; margin-top: 6px; letter-spacing: 0.5px;
  }
  .title-rule {
    width: 70px; height: 2px; background: var(--white);
    margin: 10px 0 0 auto;
  }

  /* Back */
  .back { display: flex; flex-direction: column; align-items: center; justify-content: center; gap: 18px; }
  .back-ring {
    width: 190px; height: 190px; border-radius: 50%;
    border: 10px solid var(--orange);
  }
  .back-name {
    color: var(--orange); font-weight: 900; font-size: 30px; letter-spacing: 3px;
  }
</style>
</head>
<body>
<main class="stage">

  <section class="card front" aria-label="Card front">
    <div class="brand-name">PELIKAR HIRES</div>

    <ul class="contacts">
      <li>
        <span class="contact-icon is-accent">
          <svg width="10" height="12" viewBox="0 0 10 12"><path d="M5 0a4 4 0 0 1 4 4c0 3-4 8-4 8S1 7 1 4a4 4 0 0 1 4-4z" fill="#fff"/><circle cx="5" cy="4" r="1.5" fill="#f26b21"/></svg>
        </span>
        <span>1820 Harbor Crest Drive<br>Irvine, CA 92614</span>
      </li>
      <li>
        <span class="contact-icon">
          <svg width="11" height="11" viewBox="0 0 12 12"><path d="M2 1l2 0 1 3-1.5 1a7 7 0 0 0 3.5 3.5L8 7l3 1v2a1 1 0 0 1-1 1A9 9 0 0 1 1 2a1 1 0 0 1 1-1z" fill="#555"/></svg>
        </span>
        <span>555 018-3647</span>
      </li>
      <li>
        <span class="contact-icon">
          <svg width="12" height="9" viewBox="0 0 12 9"><rect x="0.5" y="0.5" width="11" height="8" fill="none" stroke="#555"/><path d="M0.5 0.5L6 5l5.5-4.5" fill="none" stroke="#555"/></svg>
        </span>
        <span>hello@pelikarhires.com</span>
      </li>
      <li>
        <span class="contact-icon">
          <svg width="10" height="10" viewBox="0 0 10 10"><path d="M2 9L8 1M3 1h5v5" fill="none" stroke="#555" stroke-width="1.6"/></svg>
        </span>
        <span>www.pelikarhires.com</span>
      </li>
    </ul>

    <div class="accent-rule"></div>

    <p class="services">
      <strong>Luxury Restroom Trailers Rental and Sales.</strong><br>
      Weddings, Concerts, Charity, Sporting and Corp. Events.
    </p>

    <div class="person">
      <h1 class="person-name">DENNIS <strong>MOYLE</strong></h1>
      <p class="person-title">CFO</p>
      <div class="title-rule"></div>
    </div>
  </section>

  <section class="card back" aria-label="Card back">
    <div class="back-ring"></div>
    <div class="back-name">PELIKAR HIRES</div>
  </section>

</main>
</body>
</html>
```